Vorbly BIZ Card, email signature & Stationary

Professional business cards, email signatures and ms word letterhead

Target Market(s)

business owners

Industry/Entity Type

cloud hosting

Contact Information for Business Card

name title office phone number , direct line, fax email address web site

Font styles to use
Other font styles liked:
• something that compliments font in logo

```html
<!DOCTYPE html>
<html lang="en">
<head>
<meta charset="utf-8">
<title>Vorbly Stationery</title>
<link href="https://fonts.googleapis.com/css2?family=Montserrat:wght@300;400;600&family=Lato:wght@400;700&family=Great+Vibes&display=swap" rel="stylesheet">
<style>
  :root {
    --bg: #e9e6e2;
    --paper: #fbfafa;
    --ink: #1c1c1c;
    --red: #e3191f;
    --grey: #555;
    --rule: #b5b5b5;
    --dark: #1e1e1e;
  }
  * { margin: 0; padding: 0; box-sizing: border-box; }
  html, body { width: 1200px; height: 1067px; overflow: hidden; background: var(--bg); }
  .canvas { position: relative; width: 1200px; height: 1067px; font-family: 'Montserrat', sans-serif; color: var(--ink); }
  .abs { position: absolute; }
  .card { position: absolute; background: var(--paper); border-radius: 14px; box-shadow: 0 4px 10px rgba(0,0,0,.18); overflow: hidden; }
  .brand { position: absolute; font-family: 'Montserrat', sans-serif; font-weight: 300; color: var(--red); letter-spacing: -1px; line-height: 1; white-space: nowrap; }
  .person-name { font-weight: 600; white-space: nowrap; }
  .person-name .surname { color: var(--red); }
  .contact-list { list-style: none; }
  .contact-list li { display: flex; align-items: center; gap: 5px; white-space: nowrap; }
  .contact-list svg { width: 11px; height: 11px; flex: none; }
  .right { text-align: right; }

  /* front card */
  .card-front { left: 75px; top: 167px; width: 459px; height: 151px; }
  /* dark card */
  .card-dark { left: 72px; top: 348px; width: 464px; height: 267px; }
  .dark-fill { position: absolute; inset: 0; background: linear-gradient(100deg, #5a5a5a 0%, #2b2b2b 45%, #0e0e0e 100%); }
  /* back card */
  .card-back { left: 74px; top: 638px; width: 463px; height: 264px; }
  .accent-bar { position: absolute; right: 0; top: 29px; width: 9px; height: 37px; background: var(--red); }

  /* letterhead */
  .letterhead { position: absolute; left: 565px; top: 164px; width: 571px; height: 738px; background: var(--paper); box-shadow: 0 4px 12px rgba(0,0,0,.2); font-family: 'Lato', sans-serif; }
  .lh-contact { position: absolute; right: 48px; top: 30px; font-family: 'Montserrat', sans-serif; font-size: 9.5px; line-height: 13.5px; text-align: right; }
  .lh-contact .addr { margin-bottom: 3px; }
  .lh-contact .contact-list li { justify-content: flex-end; }
  .lh-contact svg { width: 8px; height: 8px; }
  .rule { position: absolute; height: 1.5px; background: var(--rule); }
  .rule-red { position: absolute; height: 3.5px; background: var(--red); }
  .recipient { position: absolute; left: 52px; top: 172px; }
  .recipient h2 { font-size: 11.5px; font-weight: 700; }
  .recipient p, .sender p { font-size: 8.5px; font-weight: 700; color: #333; margin-top: 2px; }
  .letter-date { position: absolute; right: 53px; top: 186px; font-size: 8.5px; color: #666; }
  .letter-body { position: absolute; left: 52px; top: 227px; width: 467px; font-size: 8.6px; line-height: 13.5px; color: #6b6b6b; text-align: justify; }
  .letter-body p + p { margin-top: 13.5px; }
  .signature { position: absolute; left: 54px; top: 534px; font-family: 'Great Vibes', cursive; font-size: 24px; color: #111; }
  .sender { position: absolute; left: 52px; top: 585px; }
  .sender h3 { font-size: 11.5px; font-weight: 700; }
  .sender p { color: #777; }
  .bank-line { position: absolute; left: 47px; right: 48px; top: 700px; font-size: 8.5px; color: #444; display: flex; justify-content: space-between; white-space: nowrap; }
  .bank-line .sep { color: #aaa; }
</style>
</head>
<body>
<div class="canvas">

  <!-- Front business card -->
  <section class="card card-front">
    <div class="abs" style="left:24px; top:22px;">
      <div class="person-name" style="font-size:17px;">MARCUS <span class="surname">DELANEY</span></div>
      <div style="font-size:12.5px; margin-top:2px;">Founder &amp; CEO</div>
    </div>
    <ul class="contact-list abs" style="left:24px; top:78px; font-size:12.5px; line-height:19px;">
      <li><svg viewBox="0 0 12 12"><path fill="#e3191f" d="M1 5c0-2 2-3 5-3s5 1 5 3l-2 1-1-2H4L3 6zM3 7h6l1 3H2z"/></svg>(555) 214-7730</li>
      <li><svg viewBox="0 0 12 12"><rect x="1" y="2.5" width="10" height="7" fill="#e3191f"/><path d="M1 3l5 4 5-4" stroke="#fff" fill="none"/></svg>info@vorbly.com</li>
      <li><svg viewBox="0 0 12 12"><circle cx="6" cy="6" r="5" fill="#e3191f"/><path d="M1 6h10M6 1c-3 3-3 7 0 10M6 1c3 3 3 7 0 10" stroke="#fff" stroke-width=".7" fill="none"/></svg>www.vorbly.com</li>
    </ul>
    <div class="brand" style="right:26px; top:18px; font-size:46px;">Vorbly</div>
    <div class="abs right" style="right:26px; top:96px; font-size:12px; line-height:17px;">4170 Linden Hollow Road<br>Brookvale, VA 22100</div>
  </section>

  <!-- Dark business card -->
  <section class="card card-dark">
    <div class="dark-fill" role="img" aria-label="Dark patterned card background"></div>
    <div class="brand" style="left:255px; top:166px; font-size:32px; color:#ffffff;">Vorbly</div>
  </section>

  <!-- Back business card -->
  <section class="card card-back">
    <div class="brand" style="left:17px; top:22px; font-size:46px;">Vorbly</div>
    <div class="abs right" style="right:18px; top:29px;">
      <div class="person-name" style="font-size:18px;">MARCUS <span class="surname">DELANEY</span></div>
      <div style="font-size:13.5px; margin-top:2px;">Founder &amp; CEO</div>
    </div>
    <div class="accent-bar"></div>
    <div class="abs" style="left:19px; top:136px; font-size:13.5px; line-height:19px;">4170 Linden Hollow Road<br>Brookvale, VA 22100</div>
    <ul class="contact-list abs" style="left:19px; top:183px; font-size:13.5px; line-height:20px;">
      <li><svg viewBox="0 0 12 12"><path fill="#e3191f" d="M1 5c0-2 2-3 5-3s5 1 5 3l-2 1-1-2H4L3 6zM3 7h6l1 3H2z"/></svg>(555) 214-7730</li>
      <li><svg viewBox="0 0 12 12"><rect x="1" y="2.5" width="10" height="7" fill="#e3191f"/><path d="M1 3l5 4 5-4" stroke="#fff" fill="none"/></svg>info@vorbly.com</li>
      <li><svg viewBox="0 0 12 12"><circle cx="6" cy="6" r="5" fill="#e3191f"/><path d="M1 6h10M6 1c-3 3-3 7 0 10M6 1c3 3 3 7 0 10" stroke="#fff" stroke-width=".7" fill="none"/></svg>www.vorbly.com</li>
    </ul>
  </section>

  <!-- Letterhead -->
  <section class="letterhead">
    <div class="brand" style="left:47px; top:43px; font-size:40px;">Vorbly</div>
    <div class="lh-contact">
      <div class="addr">4170 Linden Hollow Road<br>Brookvale, VA 22100</div>
      <ul class="contact-list">
        <li>(555) 214-7730<svg viewBox="0 0 12 12"><path fill="#e3191f" d="M1 5c0-2 2-3 5-3s5 1 5 3l-2 1-1-2H4L3 6zM3 7h6l1 3H2z"/></svg></li>
        <li>info@vorbly.com<svg viewBox="0 0 12 12"><rect x="1" y="2.5" width="10" height="7" fill="#e3191f"/><path d="M1 3l5 4 5-4" stroke="#fff" fill="none"/></svg></li>
        <li>www.vorbly.com<svg viewBox="0 0 12 12"><circle cx="6" cy="6" r="5" fill="#e3191f"/><path d="M1 6h10M6 1c-3 3-3 7 0 10M6 1c3 3 3 7 0 10" stroke="#fff" stroke-width=".7" fill="none"/></svg></li>
      </ul>
    </div>
    <div class="rule" style="left:47px; width:361px; top:116px;"></div>
    <div class="rule-red" style="left:408px; width:115px; top:115px;"></div>

    <div class="recipient">
      <h2>Dear. Mrs Ellen Carter Hale</h2>
      <p>Chief Director</p>
    </div>
    <div class="letter-date">Date: 24-february-2025</div>

    <div class="letter-body">
      <p>Lorem ipsum dolor sit amet, consectetur adipiscing elit, sed do eiusmod tempor incididunt ut labore et dolore magna aliqua. Sollicitudin ac orci phasellus egestas tellus rutrum tellus. Euismod elementum nisi quis eleifend quam adipiscing vitae proin sagittis. Egestas sed tempus urna et pharetra pharetra. Quis blandit turpis cursus in hac habitasse. Sed velit dignissim sodales ut eu. Ac auctor augue mauris augue neque. In arcu cursus euismod quis viverra nibh cras pulvinar mattis. Libero justo laoreet sit amet. Felis eget nunc lobortis mattis aliquam faucibus purus in. Pulvinar etiam non quam lacus suspendisse faucibus. Odio tempor orci dapibus ultrices. Velit dignissim sodales ut eu sem integer vitae justo. Fermentum et sollicitudin ac orci phasellus egestas. Pharetra vel turpis nunc eget lorem dolor sed. Sed turpis tincidunt id aliquet risus feugiat in ante. Mus mauris vitae ultricies leo integer malesuada nunc vel. Rhoncus urna neque viverra justo nec ultrices dui. Ut placerat orci nulla pellentesque dignissim enim sit amet.</p>
      <p>Bibendum arcu vitae elementum curabitur vitae nunc. Nunc pulvinar sapien et ligula ullamcorper malesuada. At elementum eu facilisis sed. Erat pellentesque adipiscing commodo elit at imperdiet dui accumsan sit. Nunc scelerisque viverra mauris in aliquam sem fringilla. In vitae turpis massa sed. Volutpat ac tincidunt vitae semper quis lectus nulla at. Massa placerat duis ultricies lacus sed turpis. Dui vivamus arcu felis bibendum ut tristique et egestas. Blandit aliquam etiam erat velit scelerisque in dictum non consectetur. Id neque aliquam vestibulum morbi blandit cursus risus at. Sed egestas egestas fringilla phasellus faucibus scelerisque eleifend donec. Ornare quam viverra orci sagittis eu volutpat odio facilisis. Volutpat sed cras ornare arcu dui vivamus arcu. Interdum consectetur libero id faucibus nisl.</p>
      <p>Viverra mauris in aliquam sem. Mattis molestie a iaculis at erat pellentesque adipiscing commodo elit. Sit amet volutpat consequat mauris nunc. Aliquam nulla facilisi cras fermentum. Sed turpis tincidunt id aliquet risus feugiat. Augue neque gravida in fermentum et sollicitudin ac orci.</p>
    </div>

    <div class="signature">Peter alan voss</div>
    <div class="sender">
      <h3>Peter Alan Voss</h3>
      <p>Chief Director</p>
    </div>

    <div class="rule-red" style="left:47px; width:115px; top:854px; top:689px;"></div>
    <div class="rule" style="left:162px; width:361px; top:690px;"></div>
    <div class="bank-line">
      <span>Bank: Nordbank</span><span class="sep">/</span>
      <span>Kontoinhaber: Lena Hartwig</span><span class="sep">/</span>
      <span>IBAN: DE00 1234 5678 9012 3456 78</span><span class="sep">/</span>
      <span>BIC: NRDBDEFFXXX</span>
    </div>
  </section>

</div>
</body>
</html>
```